Tech business card design

We need an amazing business card design for our new business 'Brakka' a marketing tech startup based in Sydney, Australia. We provide an online marketplace for businesses to search and buy advertising media, connect with service providers and learn more about marketing. We wish to communicate 'cool tech', reliability and professionalism and design based around our logo.

Target Market(s)

Business Owners

Contact Information for Business Card

Name
Position
Email Address
Website
Phone Number

Font styles to use
Other font styles liked:
• Avenir & Avenir Next

Colors

Designer to choose colors to be used in the design.

```html
<!DOCTYPE html>
<html lang="en">
<head>
<meta charset="utf-8">
<title>Brakka Business Card</title>
<link href="https://fonts.googleapis.com/css2?family=Roboto:wght@400;500;700;900&display=swap" rel="stylesheet">
<style>
  :root {
    --backdrop: #1b1a40;
    --navy: #1f1c4d;
    --card-back: #221f57;
    --pattern-light: #2f2c68;
    --paper: #f7f7f7;
    --paper-edge: #ececec;
    --ink-muted: #555560;
    --rule: #a9a9b0;
    --white: #ffffff;
  }
  * { margin: 0; padding: 0; box-sizing: border-box; }
  html, body {
    width: 1200px; height: 869px; overflow: hidden;
    background: var(--backdrop);
    font-family: "Roboto", Arial, sans-serif;
  }
  .canvas { position: relative; width: 1200px; height: 869px; }
  .card {
    position: absolute; top: 208px; width: 296px; height: 518px;
    overflow: hidden;
  }
  .card--front {
    left: 266px;
    background: linear-gradient(180deg, var(--white), var(--paper) 60%, var(--paper-edge));
    text-align: center; color: var(--navy);
  }
  .card--back { left: 639px; background: var(--card-back); }

  .wordmark {
    position: absolute; top: 78px; left: 0; right: 0;
    font-weight: 900; font-size: 62px; letter-spacing: -1px; line-height: 1;
    color: var(--navy);
  }
  .person { position: absolute; top: 226px; left: 0; right: 0; }
  .person__name { font-weight: 500; font-size: 28px; line-height: 1.1; }
  .person__role { font-size: 18px; color: var(--ink-muted); margin-top: 2px; }

  .contact { position: absolute; left: 0; right: 0; color: var(--ink-muted); font-size: 14.5px; }
  .contact__icon { position: absolute; left: 0; right: 0; height: 18px; display: flex; justify-content: center; align-items: center; gap: 8px; }
  .contact__rule { width: 30px; height: 1.5px; background: var(--rule); }
  .contact__icon svg { display: block; fill: var(--navy); }

  .pattern {
    position: absolute; inset: 0;
    background: repeating-linear-gradient(-55deg, var(--card-back) 0 22px, var(--pattern-light) 22px 44px);
    opacity: 0.55;
  }
  .back-mark {
    position: absolute; left: 221px; top: 428px;
    transform: translate(-50%, -50%) rotate(-35deg);
    font-weight: 900; font-size: 44px; letter-spacing: -0.5px; line-height: 1;
    color: var(--white);
  }
</style>
</head>
<body>
<main class="canvas">
  <section class="card card--front">
    <div class="wordmark">brakka</div>

    <div class="person">
      <div class="person__name">Liam Carver</div>
      <div class="person__role">Owner</div>
    </div>

    <div class="contact__icon" style="top:321px">
      <svg width="11" height="17" viewBox="0 0 11 17"><path d="M2 0h7a2 2 0 0 1 2 2v13a2 2 0 0 1-2 2H2a2 2 0 0 1-2-2V2a2 2 0 0 1 2-2zm0 2.5v10h7v-10zm3.5 11.2a.9.9 0 1 0 0 1.8.9.9 0 0 0 0-1.8z"/></svg>
    </div>
    <div class="contact" style="top:349px">123 456 7890</div>

    <div class="contact__icon" style="top:378px">
      <span class="contact__rule"></span>
      <svg width="14" height="10" viewBox="0 0 14 10"><path d="M0 0h14v1.5L7 6 0 1.5z"/><path d="M0 3l7 4.5L14 3v7H0z"/></svg>
      <span class="contact__rule"></span>
    </div>
    <div class="contact" style="top:406px">info@yourwebsite.com</div>

    <div class="contact__icon" style="top:437px">
      <span class="contact__rule"></span>
      <svg width="14" height="14" viewBox="0 0 14 14" fill="none" stroke="currentColor" style="color:var(--navy);fill:none"><circle cx="7" cy="7" r="6" stroke-width="1.4"/><ellipse cx="7" cy="7" rx="2.6" ry="6" stroke-width="1.2"/><path d="M1 7h12M2 4h10M2 10h10" stroke-width="1.1"/></svg>
      <span class="contact__rule"></span>
    </div>
    <div class="contact" style="top:464px">www.yourwebsite.com</div>
  </section>

  <section class="card card--back">
    <div class="pattern" role="img" aria-label="Faint diagonal repeat of the Brakka name across the card"></div>
    <div class="back-mark">brakka</div>
  </section>
</main>
</body>
</html>
```